Candle Box & Belly Band Design

Design Candle Box for Soy Candles along with a belly band design that can be used on off the shelf coloured boxes. It is for a premium brand of candle - so i want the packaging to reflect this. I have included must haves below.

The candle boxes will be a few different sizes, but for the purpose of the design it would be something like a cube 12 x 12 x 12 cms

The belly band for standard boxes to be something like 5cm wide on a 12 x 12 x 12cms cube box that goes all the way around the top to the bottom - holding the lid on and providing all the relevant information. Example of box with belly band uploaded

Our company Name : Hazel & Pip - our logo is uploaded

Target Market(s)

Premium Candle Buyers

Colors

Designer to choose colors to be used in the design.

Requirements
Must have
• Must have our logo - our logo can be in any colour
• Must state:
• Soy Candle, Hand Poured, Made in Melbourne,
• A space for the fragrance, size and burn time.
• For this project use Lime, Coconut & Elderfllower, 300grams, 50 Hour burn Time

```html
<!DOCTYPE html>
<html lang="en">
<head>
<meta charset="utf-8">
<title>Hazel &amp; Pip Soy Candle – Belly Band</title>
<link rel="stylesheet" href="https://fonts.googleapis.com/css2?family=Poiret+One&family=Roboto:wght@400;500&family=Kaushan+Script&display=swap">
<style>
  :root {
    --canvas: #f3f3f3;
    --box-yellow: #e8dc34;
    --box-shade: #d9cc2c;
    --band-white: #f2f2f2;
    --ink: #3a3a3a;
    --panel-grey: #e4e4e4;
    --icon-white: #fafafa;
  }
  * { box-sizing: border-box; margin: 0; padding: 0; }
  html, body { width: 1200px; height: 1056px; overflow: hidden; }
  body {
    background: var(--canvas);
    font-family: "Roboto", sans-serif;
    color: var(--ink);
    position: relative;
  }
  .face {
    position: absolute;
    top: 268px;
    width: 520px;
    height: 520px;
    background: var(--box-yellow);
  }
  .face--top { left: 620px; background: var(--box-shade); }
  .face--front { left: 60px; }
  .face-label {
    position: absolute;
    top: 800px;
    font-size: 13px;
    letter-spacing: 2px;
    text-transform: uppercase;
    color: #9a9a9a;
  }
  .band {
    position: absolute;
    left: 160px;
    top: 0;
    width: 200px;
    height: 520px;
    background: var(--band-white);
    text-align: center;
  }

  /* front band */
  .brand-frame {
    position: absolute;
    left: 37px; top: 21px;
    width: 126px; height: 186px;
    border: 3px solid var(--ink);
    padding: 4px;
  }
  .brand-frame-inner {
    width: 100%; height: 100%;
    border: 1px solid var(--ink);
    display: flex; align-items: flex-end; justify-content: center;
    padding-bottom: 14px;
  }
  .brand-name {
    font-family: "Roboto", sans-serif;
    font-weight: 500;
    font-size: 17px;
    color: var(--ink);
  }
  .product-title {
    position: absolute;
    left: 20px; right: 20px;
    top: 222px;
    padding: 8px 0;
    border-top: 1px solid var(--ink);
    border-bottom: 1px solid var(--ink);
    font-family: "Poiret One", sans-serif;
    font-size: 28px;
    line-height: 34px;
  }
  .tagline {
    position: absolute;
    left: 0; right: 0; top: 310px;
    font-size: 14px;
  }
  .fragrance-panel {
    position: absolute;
    left: 0; right: 0; top: 338px;
    height: 96px;
    background: var(--box-yellow);
    border-top: 2px solid var(--ink);
    border-bottom: 2px solid var(--ink);
  }
  .fragrance-icon {
    position: absolute;
    left: 14px; top: 16px;
    width: 56px; height: 62px;
    background: var(--icon-white);
    border-radius: 6px;
  }
  .fragrance-notes {
    position: absolute;
    left: 82px; top: 8px;
    text-align: left;
    font-family: "Kaushan Script", cursive;
    font-size: 17px;
    line-height: 26px;
  }
  .details-panel {
    position: absolute;
    left: 0; right: 0; top: 434px; bottom: 0;
    background: var(--panel-grey);
    padding-top: 10px;
    font-size: 13px;
    line-height: 24px;
  }
  .details-panel .size {
    display: inline-block;
    padding: 0 16px;
    border-bottom: 1px solid var(--ink);
    line-height: 20px;
  }

  /* top band */
  .band--top .brand-name {
    position: absolute; left: 0; right: 0; top: 110px;
    font-size: 17px;
  }
  .band--top .brand-square {
    position: absolute; left: 88px; top: 70px;
    width: 24px; height: 24px;
    background: var(--ink);
  }
  .band--top .product-title {
    top: 150px;
    font-size: 24px;
    line-height: 28px;
    left: 28px; right: 28px;
  }
  .band--top .fragrance-icon {
    position: absolute; left: 72px; top: 222px;
    width: 56px; height: 34px;
    background: var(--ink);
  }
  .band--top .fragrance-line {
    position: absolute; left: 0; right: 0; top: 276px;
    font-family: "Kaushan Script", cursive;
    font-size: 13px;
  }
</style>
</head>
<body>

  <section class="face face--front">
    <div class="band band--front">
      <div class="brand-frame">
        <div class="brand-frame-inner">
          <span class="brand-name">Hazel &amp; Pip</span>
        </div>
      </div>
      <h1 class="product-title">Soy Candle</h1>
      <p class="tagline">Hand Poured</p>
      <div class="fragrance-panel">
        <div class="fragrance-icon" role="img" aria-label="Candle with flower icon"></div>
        <p class="fragrance-notes">·Lime·<br>·Coconut·<br>·Elderfllower·</p>
      </div>
      <div class="details-panel">
        <p>Made in Melbourne</p>
        <p class="size">300 gr.</p>
        <p>50 Hour burn Time</p>
      </div>
    </div>
  </section>

  <section class="face face--top">
    <div class="band band--top">
      <div class="brand-square"></div>
      <span class="brand-name">Hazel &amp; Pip</span>
      <h2 class="product-title">Soy Candle</h2>
      <div class="fragrance-icon" role="img" aria-label="Candle with flower icon"></div>
      <p class="fragrance-line">·Lime·Coconut·Elderfllower·</p>
    </div>
  </section>

</body>
</html>
```